Verdant Holdings SA Business Cards

Dear all,
Thank you for reading my brief and project. My company is doing doing advisory in real estate and to comapnies + real estates services as asset management, brokerage, development etc.
I would like to get a business card for my company which is clear, professionnal and serious.
Please have a look to the attachement to see the logos of the company

Industry/Entity Type

Real Estate

Contact Information for Business Card

I would like to have in the business card the following
Principal side:
- Logo of the company (or Monogram)
- First and Last Name (Marcel Tobler)
- Mobile number
- email address

Second side:
- Address (Chemin des Vergers 17, 1292 Chambésy - Switzerland)
- website (www.verdantholdings.ch)

Requirements
Must have
• Refer to the typeface and logo colors

```html
<!DOCTYPE html>
<html lang="en">
<head>
<meta charset="utf-8">
<title>Verdant Holdings SA – Business Cards</title>
<link rel="stylesheet" href="https://fonts.googleapis.com/css2?family=Open+Sans:wght@400;600;700&display=swap">
<style>
  :root {
    --page: #e4e6e9;
    --navy: #34475c;
    --navy-map: #3d5168;
    --slate: #3a4656;
    --blue: #1f6fb2;
    --ink: #2f3a46;
    --white: #ffffff;
    --card-white: #f7f7f8;
  }
  * { margin: 0; padding: 0; box-sizing: border-box; }
  html, body {
    width: 1200px; height: 1021px; overflow: hidden;
    background: var(--page);
    font-family: "Open Sans", Arial, sans-serif;
  }
  .canvas { position: relative; width: 1200px; height: 1021px; }

  .card {
    position: absolute;
    width: 620px; height: 400px;
    border-radius: 4px;
    box-shadow: 0 10px 30px rgba(0,0,0,.18), 0 2px 6px rgba(0,0,0,.12);
    overflow: hidden;
  }

  /* back side */
  .card-back { left: 420px; top: 70px; background: var(--navy); }
  .world-map {
    position: absolute; left: 40px; top: 40px; width: 540px; height: 300px;
    border-radius: 40%;
    background: radial-gradient(ellipse at center, var(--navy-map) 0%, rgba(61,81,104,0) 72%);
  }
  .back-brand {
    position: absolute; left: 0; right: 0; top: 150px;
    display: flex; align-items: center; justify-content: center; gap: 16px;
  }
  .brand-dot { width: 18px; height: 18px; border-radius: 50%; }
  .card-back .brand-dot { background: var(--white); }
  .back-brand .brand-name {
    color: var(--white); font-size: 34px; font-weight: 600; letter-spacing: 2px;
    text-transform: uppercase;
  }
  .back-web {
    position: absolute; left: 0; right: 0; top: 310px; text-align: center;
    color: var(--white); font-size: 15px; font-weight: 600; letter-spacing: 3.5px;
  }

  /* front side */
  .card-front { left: 160px; top: 560px; background: linear-gradient(100deg, var(--white) 0%, var(--card-white) 60%, #ececee 100%); }
  .front-brand {
    position: absolute; left: 48px; top: 46px;
    display: flex; align-items: center; gap: 12px;
  }
  .card-front .brand-dot { background: var(--slate); }
  .front-brand .brand-name {
    color: var(--slate); font-size: 24px; font-weight: 600; letter-spacing: 1.5px;
    text-transform: uppercase;
  }
  .person { position: absolute; left: 48px; top: 150px; }
  .person-name { color: var(--blue); font-size: 22px; font-weight: 700; line-height: 1.1; }
  .person-role { color: var(--ink); font-size: 16px; margin-top: 2px; }
  .person-rule { width: 40px; height: 1px; background: var(--ink); margin: 12px 0 14px; }
  .contacts { list-style: none; }
  .contacts li {
    display: flex; align-items: center; gap: 8px;
    color: var(--ink); font-size: 16px; line-height: 24px;
  }
  .contacts svg { width: 14px; height: 14px; flex: none; }
  .contacts .accent { color: var(--blue); }
  .address {
    position: absolute; left: 360px; top: 285px;
    color: var(--ink); font-size: 16px; line-height: 21px; font-style: normal;
  }
</style>
</head>
<body>
<main class="canvas">

  <section class="card card-back" aria-label="Card back">
    <div class="world-map" role="img" aria-label="Faint world map in the background"></div>
    <div class="back-brand">
      <span class="brand-dot"></span>
      <span class="brand-name">Verdant Holdings</span>
    </div>
    <p class="back-web">www.verdantholdings.ch</p>
  </section>

  <section class="card card-front" aria-label="Card front">
    <div class="front-brand">
      <span class="brand-dot"></span>
      <span class="brand-name">Verdant Holdings</span>
    </div>

    <div class="person">
      <h1 class="person-name">Marcel Tobler</h1>
      <p class="person-role">Founder</p>
      <div class="person-rule"></div>
      <ul class="contacts">
        <li>
          <svg viewBox="0 0 14 14" aria-hidden="true"><rect x="3.5" y="0.8" width="7" height="12.4" rx="1.2" fill="none" stroke="#1f6fb2" stroke-width="1.2"/><line x1="6" y1="11" x2="8" y2="11" stroke="#1f6fb2" stroke-width="1.2"/></svg>
          +41 79 418 26 53
        </li>
        <li>
          <svg viewBox="0 0 14 14" aria-hidden="true"><rect x="0.8" y="2.5" width="12.4" height="9" fill="none" stroke="#1f6fb2" stroke-width="1.2"/><polyline points="1,3 7,8 13,3" fill="none" stroke="#1f6fb2" stroke-width="1.2"/></svg>
          marcel.tobler@verdantholdings.ch
        </li>
        <li>
          <svg viewBox="0 0 14 14" aria-hidden="true"><circle cx="7" cy="7" r="6" fill="none" stroke="#1f6fb2" stroke-width="1.2"/><ellipse cx="7" cy="7" rx="2.6" ry="6" fill="none" stroke="#1f6fb2" stroke-width="1"/><line x1="1" y1="7" x2="13" y2="7" stroke="#1f6fb2" stroke-width="1"/></svg>
          <span>www.<span class="accent">verdantholdings</span>.ch</span>
        </li>
      </ul>
    </div>

    <address class="address">
      Chemin des Vergers 17<br>
      1292 Chambésy<br>
      Switzerland
    </address>
  </section>

</main>
</body>
</html>
```